Cloud Hosting Startup, and Panthers!

Hi!

We are corvalnest.com

A new hosting service that aims to provide awesome hosting and a bit of development work for free to get people set up.

We have decided on a logo and a theme. Awesome Panthers.

So, we are all about Panthers =)

-

We greatly desire a super super cool vector scene for the homepage. We love mountains, blue mountains, and green grass. Panthers hiding in long grass or leaping through the air to accentuate the coolness of our service would also be most appreciated.

Panthers hiding amongst crisp blue mountains, or hanging out on snowy mountain peaks thinking Panther things.

Or in green grassy jungles, hiding next to rocks and scaring zebras.

Or something =)

-

For the sub pages we would just like a style guide, showing the standard h1,h2's and some other items for layout.

As you can see at corvalnest.com we are almost ready for launch, we are web developers ourselves, and so we got the site design as far as we could.

We have our software written and ready for customers, however the site just doesn't tell you what its about from a glance! That's why we need you. So, Panthers, Cool cool, sweet Panthers to accentuate our cool new launch and hosting service.

We have included the vectors used and the site design as it stands. We would like to remain with the three items 'mini-panther', 'standard panther', and 'epic panther' from this page: corvalnest.com/signup

Apart from the epic panthers, and some variation of the panthers used for the logo, we are not fully attached other elements. We have gone with a strong red white and black, but we are just wacky developers, we need your help!

Looking forward to some great designs! If you are inspired by Panthers and super cool web hosting, this project is for you.

Thanks!!

The Corvalnest.com Team

Project payment has been guaranteed, we are committed to a result

Just a quick update based on a designer question:

We have spent many weeks of drinking coffee and coding, we have finished all the coding, all done!

If you take a look at Corvalnest.com you can see the result.

Basically we are looking for someone to take what we have already done (files attached of all our work) and make it less like a developer designed it, which is what happened along the way =)

Help us tavo ren malduk ..
 

Basically, we are looking for increased awesome.

We have a really cool, cheap hosting and template product offering, we would love it if someone could breathe the life of Panther into it =)

Ok,

Thanks =)

Sorry, one more update =)

Basically we are not looking for an entire site re-design, the major thing is a cool scene for the homepage with panthers and mountains =)

We are just looking for a touch up, a polish, someone to give it the design magic that communicates the message in the copy we have written. We have worked out our product and completed it, we just need someone to help us bring it to the market.

Ok, thanks!

One final update then we will return to coding our Panther and leave you all alone =)

Our internet heroes are: http://www.drelvix.com/

We love them, their purple colour scheme makes us unhappy, but we so love their signup and plan selection process.

Ok!

Thanks so much, from Corvalnest Team

Reason: Deadline has been extended one day to allow new designers time to prepare some panther concepts. We will also use the extra day to await funds transfer to increase the budget of the project and hopefully add a 2nd place prize (pixelbazaar fees permitting) Thanks everyone! Gareth Corvalnest.com

Thanks all!

Reason: Deadline extended a further one day, 1st prize and 2nd prize payments have been updated today, looking forward to submissions! Thanks everyone

Just an update, really great designs coming in, loving all the panther concepts =)

We will award the competition on the 21st, and we have two prizes now, we will award one based on visual design and appeal (the most stunning panther), and one based on use of copy and user interface (the easiest panther)

Ok!

Thanks, hope you have enjoyed designing, we have definitely enjoyed receiving designs to bring our idea to life

Thanks!!

Gareth

Corvalnest

Sorry!

One more update, we have added a third prize now of $100 

We love the designs too much not to make use of them =)

Ok!

Last update =)

Thanks all

Hi All,

Wonderful work, thanks everyone for feedback and revisions

We have only one day of the competition left, we are asking now for final submissions, we have provided a style guide template here:

http://corvalnest.com/web_final_template.psd

The team will judge the competition tomorrow, we have now 3 prizes and we will add 2 participation payments as a fourth prize as we have asked some designers for some strange requests =)

Ok!

Looking forward to final submissions with the home page and style guide, thanks again!

Gareth

Corvalnest

Target Market(s)

Tech savvy people, but not tech geniuses, young fun people who at least know what web-hosting is

Industry/Entity Type

Software

Requirements
Must have
• - super super cool vector landscape for the homepage
- some number of sub pages, in accordance with the site structure as it stands

```html
<!DOCTYPE html>
<html lang="en">
<head>
<meta charset="utf-8">
<title>Corvalnest — Powerful &amp; Instant Websites</title>
<link rel="stylesheet" href="https://fonts.googleapis.com/css2?family=Gelasio:ital,wght@0,400;0,700;1,400;1,700&family=PT+Sans:wght@400;700&family=Playfair+Display:wght@900&display=swap">
<style>
  :root {
    --ink: #1e1e1e;
    --page: #f3f3f3;
    --card: #ffffff;
    --red: #e8493a;
    --bar: #050505;
    --footer: #2b2b2b;
    --footer-line: #d9d9d9;
    --muted: #8a8a8a;
    --sky-light: #cfeaf8;
    --sky: #7fc6ee;
    --peak: #5a7fc4;
    --forest: #0f1a30;
    --disc: #c9c9c9;
  }
  * { box-sizing: border-box; margin: 0; padding: 0; }
  html, body { width: 978px; height: 1200px; overflow: hidden; }
  body {
    position: relative;
    background: var(--page);
    color: var(--ink);
    font-family: "Gelasio", Georgia, serif;
  }
  .abs { position: absolute; }

  /* top bar */
  .top-bar { left: 0; top: 0; width: 978px; height: 36px; background: var(--bar); border-bottom: 2px solid #cfcfcf; }
  .brand-tab {
    left: 243px; top: 0; width: 116px; height: 64px;
    background: var(--red); box-shadow: 0 2px 5px rgba(0,0,0,.35);
    display: flex; flex-direction: column; align-items: center; justify-content: flex-end;
    padding-bottom: 10px; gap: 7px;
  }
  .brand-tab .brand-dot { width: 14px; height: 14px; border-radius: 50%; background: #fff; }
  .brand-tab .brand-name { font-family: "PT Sans", sans-serif; font-weight: 700; color: #fff; font-size: 13px; letter-spacing: .3px; }
  .main-nav { right: 255px; top: 13px; display: flex; font-family: "PT Sans", sans-serif; font-size: 6.5px; }
  .main-nav a { color: #d8d8d8; text-decoration: none; padding: 0 7px; border-left: 1px solid #3a3a3a; line-height: 10px; }
  .main-nav a:first-child { border-left: 0; }

  /* hero */
  .hero-scene {
    left: 15px; top: 62px; width: 948px; height: 210px;
    background:
      linear-gradient(180deg, rgba(243,243,243,1) 0%, rgba(243,243,243,0) 30%),
      linear-gradient(180deg, var(--sky-light) 20%, var(--sky) 45%, var(--peak) 65%, var(--forest) 92%);
    -webkit-mask-image: linear-gradient(90deg, transparent 0, #000 4%, #000 96%, transparent 100%);
            mask-image: linear-gradient(90deg, transparent 0, #000 4%, #000 96%, transparent 100%);
  }
  .hero-title { left: 0; top: 80px; width: 930px; text-align: center; }
  .hero-title .kicker { font-style: italic; font-weight: 700; font-size: 19px; color: #333; line-height: 22px; }
  .hero-title .kicker em { color: var(--red); text-transform: uppercase; }
  .hero-title h1 { font-family: "Playfair Display", Georgia, serif; font-weight: 900; font-size: 40px; line-height: 40px; color: #2f2f2f; letter-spacing: 1px; }
  .offer-ribbon {
    left: 697px; top: 96px; width: 145px; height: 28px;
    background: var(--red); color: #fff; transform: rotate(-6deg);
    font-style: italic; font-weight: 700; font-size: 6.3px; line-height: 8px; text-align: center;
    padding: 6px 12px 0; box-shadow: 0 2px 3px rgba(0,0,0,.25);
    clip-path: polygon(0 0, 100% 0, 94% 50%, 100% 100%, 0 100%);
  }

  /* service tiles */
  .service-tiles { left: 245px; top: 294px; display: flex; gap: 4px; }
  .service-tile {
    width: 119px; height: 91px; background: var(--card);
    display: flex; flex-direction: column; align-items: center; justify-content: flex-end; padding-bottom: 23px;
    font-style: italic; font-weight: 700; font-size: 10px;
  }
  .service-tile svg { margin-bottom: 6px; }

  /* feature discs */
  .feature-disc { width: 80px; height: 80px; border-radius: 50%; background: var(--card); display: flex; align-items: center; justify-content: center; }

  /* feature copy */
  .feature-copy { width: 128px; }
  .feature-copy h3 { font-style: italic; font-weight: 400; font-size: 11px; margin-bottom: 10px; }
  .feature-copy p { font-style: italic; font-size: 7.8px; line-height: 9.8px; text-align: justify; color: #333; }

  /* overview */
  .overview { right: 418px; top: 702px; text-align: right; font-style: italic; }
  .overview h3 { font-weight: 400; font-size: 11px; margin-bottom: 8px; }
  .overview li { list-style: none; font-size: 7.8px; line-height: 9.8px; color: #333; }
  .terms-disc {
    left: 611px; top: 714px; width: 76px; height: 76px; border-radius: 50%;
    background: var(--disc); display: flex; align-items: center; justify-content: center;
    text-align: center; font-style: italic; font-size: 10px; line-height: 13px; color: #333;
    text-decoration: none;
  }

  /* footer */
  .site-footer { left: 0; top: 896px; width: 978px; height: 304px; background: var(--footer); border-top: 3px solid var(--footer-line); }
  .plans-ribbon {
    left: 362px; top: 866px; width: 262px; height: 36px;
    background: var(--red); color: #fff; transform: rotate(-11deg);
    font-style: italic; font-weight: 700; font-size: 10px; line-height: 36px; text-align: center;
    clip-path: polygon(0 0, 100% 0, 94% 50%, 100% 100%, 0 100%, 5% 50%);
    box-shadow: 0 3px 4px rgba(0,0,0,.3);
  }
  .footer-heading { font-family: "PT Sans", sans-serif; font-weight: 700; font-size: 7.5px; color: #fff; }
  .footer-links { left: 240px; top: 964px; width: 100px; text-align: center; list-style: none; font-family: "PT Sans", sans-serif; font-size: 7px; line-height: 15px; }
  .footer-links a { color: var(--muted); text-decoration: none; }
  .social-disc { width: 27px; height: 27px; border-radius: 50%; border: 2px solid #777; background: #555; }
  .contact-field { background: #fff; border: 0; font-family: "PT Sans", sans-serif; font-size: 5.5px; color: #888; padding: 6px 6px; }
  .send-button { left: 695px; top: 1023px; width: 38px; height: 14px; background: var(--red); color: #fff; font-family: "PT Sans", sans-serif; font-size: 6px; text-align: center; line-height: 14px; }
  .footer-brand { left: 0; top: 1060px; width: 978px; display: flex; flex-direction: column; align-items: center; gap: 12px; }
  .footer-brand .brand-dot { width: 22px; height: 22px; border-radius: 50%; background: var(--red); }
  .footer-brand .brand-name { font-family: "PT Sans", sans-serif; font-weight: 700; font-size: 17px; color: #fff; }
  .copyright { left: 0; top: 1146px; width: 978px; text-align: center; font-family: "PT Sans", sans-serif; font-size: 6px; color: var(--muted); }
</style>
</head>
<body>

<header>
  <div class="abs top-bar"></div>
  <div class="abs brand-tab">
    <span class="brand-dot"></span>
    <span class="brand-name">CORVALNEST</span>
  </div>
  <nav class="abs main-nav">
    <a href="#">HOME</a>
    <a href="#">PLANS &amp; PRICING</a>
    <a href="#">SIGN UP</a>
    <a href="#">CONTACT</a>
  </nav>
</header>

<section class="hero">
  <div class="abs hero-scene" role="img" aria-label="Vector landscape of snowy blue mountains and a dark pine forest, with a winged panther and a leaping panther among soaring birds"></div>
  <div class="abs hero-title">
    <p class="kicker">powerful &amp; <em>instant</em></p>
    <h1>WEBSITES</h1>
  </div>
  <div class="abs offer-ribbon">Template, Domain, Hosting and Email package for under $20</div>
</section>

<section class="abs service-tiles">
  <div class="service-tile">
    <svg width="82" height="28" viewBox="0 0 82 28"><g fill="#1e1e1e"><circle cx="26" cy="16" r="10"/><circle cx="40" cy="12" r="12"/><circle cx="56" cy="17" r="8"/><rect x="2" y="18" width="78" height="8" rx="4"/></g></svg>
    Hosting
  </div>
  <div class="service-tile">
    <svg width="32" height="32" viewBox="0 0 32 32"><circle cx="16" cy="16" r="15" fill="#e8493a"/><path d="M8 9c4 1 6 4 5 7s2 4 1 8M18 5c1 3 5 3 7 6s-2 5 0 8" stroke="#fff" stroke-width="3" fill="none"/></svg>
    Domain &amp; Email
  </div>
  <div class="service-tile">
    <svg width="56" height="32" viewBox="0 0 56 32"><rect x="14" y="0" width="28" height="32" fill="#1e1e1e"/><path d="M0 12h18v10H0l5-5z M56 12H38v10h18l-5-5z" fill="#1e1e1e"/></svg>
    Template
  </div>
  <div class="service-tile">
    <svg width="50" height="30" viewBox="0 0 50 30"><path d="M48 2 30 6 12 20l8 8L34 14z" fill="#1e1e1e"/><path d="M14 14 4 14 0 20l10-1zM26 26v8l-6 2 1-8z" fill="#1e1e1e"/></svg>
    Launch
  </div>
</section>

<section class="features">
  <div class="abs feature-disc" style="left:284px;top:423px">
    <svg width="50" height="22" viewBox="0 0 50 22"><g fill="#1e1e1e"><circle cx="18" cy="10" r="6"/><circle cx="27" cy="8" r="7"/><circle cx="36" cy="11" r="5"/><rect x="2" y="11" width="46" height="6" rx="3"/></g><path d="M20 17h10l-5 4z" fill="#e8493a"/></svg>
  </div>
  <div class="abs feature-disc" style="left:449px;top:423px">
    <svg width="32" height="32" viewBox="0 0 32 32"><circle cx="16" cy="16" r="15" fill="#1e1e1e"/><path d="M8 9c4 1 6 4 5 7s2 4 1 8M18 5c1 3 5 3 7 6s-2 5 0 8" stroke="#fff" stroke-width="3" fill="none"/></svg>
  </div>
  <div class="abs feature-disc" style="left:610px;top:423px">
    <svg width="38" height="26" viewBox="0 0 38 26"><rect x="8" y="0" width="22" height="26" fill="#1e1e1e"/><path d="M0 10h38l-4 3 4 3H0l4-3z" fill="#e8493a"/></svg>
  </div>

  <article class="abs feature-copy" style="left:276px;top:545px">
    <h3>Hosting</h3>
    <p>Control wheel is a lightweight Kestrel plugin what helps you to create knob style interfaces. With it's easy to use method you can create a knob interface with ease. All modern browsers, smart phones and tablets are supported.</p>
  </article>
  <article class="abs feature-copy" style="left:429px;top:545px">
    <h3>Domain &amp; Email</h3>
    <p>The whole functionality of this plugin is represented on top of this page, try out our examples on various browsers, smart phones, tablets to see the tremendous browser and device support.</p>
  </article>
  <article class="abs feature-copy" style="left:581px;top:545px">
    <h3>Templates</h3>
    <p>We get you up and running with beautiful templates, integrated with simple and powerful website management software.</p>
  </article>
</section>

<section class="abs overview">
  <h3>Quick Overview</h3>
  <ul>
    <li>Easy to Implement</li>
    <li>Detailed Documentation</li>
    <li>Lots of Ready to Use Examples (just copy and paste)</li>
    <li>Good Browser Support (Vexa 7+, Brightfox, Savanna, Halcyon, Cantata)</li>
    <li>Support for Smart phones (Zephon &amp; Andrix)</li>
    <li>Support for Tablets (Zepad &amp; Andrix powered tablets)</li>
    <li>PSD's included</li>
  </ul>
</section>
<a class="abs terms-disc" href="#">Terms and<br>conditions</a>

<footer>
  <div class="abs site-footer"></div>
  <div class="abs plans-ribbon">View our Plans and Templates</div>

  <h4 class="abs footer-heading" style="left:240px;top:949px;width:100px;text-align:center">CORVALNEST</h4>
  <ul class="abs footer-links">
    <li><a href="#">Home</a></li>
    <li><a href="#">Plans &amp; Pricing</a></li>
    <li><a href="#">Sign Up</a></li>
    <li><a href="#">Contact</a></li>
  </ul>

  <span class="abs social-disc" style="left:385px;top:969px"></span>
  <span class="abs social-disc" style="left:423px;top:969px"></span>

  <h4 class="abs footer-heading" style="left:581px;top:949px">CONTACT CORVALNEST</h4>
  <div class="abs contact-field" style="left:494px;top:966px;width:97px;height:21px">Contact Name</div>
  <div class="abs contact-field" style="left:494px;top:991px;width:97px;height:20px">Contact Email</div>
  <div class="abs contact-field" style="left:595px;top:966px;width:138px;height:45px">Message</div>
  <div class="abs send-button">Send</div>

  <div class="abs footer-brand">
    <span class="brand-dot"></span>
    <span class="brand-name">CORVALNEST</span>
  </div>
  <p class="abs copyright">© 2012 | Corvalnest.com</p>
</footer>

</body>
</html>
```